QM active wear

Hey There

QM is a brand new active wear Sydney base company. our clothe design by professional dancers & athletics. pushing the niche market of active wear. the products we have is cool fashionable functional Eco friendly!!!

it caters male and female. who stays active and wants to be chic at the same time.
we would like to be associate with K-8 & Coastal garments & Vorn kind of brands.

i need you guys to use the existing logo to restructure it. turn it into consistent format that can be shared through out all the electronic business stationery. pls refer to all the photos i have upload in this brief. hopefully it'll gives you guys more of what i like i needs to be done.

PS: business card material specifications needs to be provided.
just so send the details to the printing company without explain too much.

Cheers

Industry/Entity Type

Electronic

Requirements
Must have
• It needs be more readable. clean. current. pop. fashionable.
interesting details across the broad for all electronic stationary.

for you to think about it and working on : company's business letters, order forms, its notices and other official publications, promissory notes, endorsements, cheques and orders for money or goods purporting to be signed by, or on behalf of, the company invoices, receipts websites

```html
<!DOCTYPE html>
<html lang="en">
<head>
<meta charset="utf-8">
<title>QM active wear — business card</title>
<link href="https://fonts.googleapis.com/css2?family=Archivo:wght@300;400;800&display=swap" rel="stylesheet">
<style>
  :root {
    --backdrop: #e9e7e4;
    --ink: #0a0a0a;
    --paper-white: #ffffff;
    --denim-light: #7b9ae0;
    --denim-mid: #4f74cf;
    --denim-deep: #2a3f86;
    --charcoal: #3a3a3a;
    --muted: #cfcfcf;
  }
  * { box-sizing: border-box; margin: 0; padding: 0; }
  html, body {
    width: 804px; height: 1200px; overflow: hidden;
    background: var(--backdrop);
    font-family: "Archivo", Arial, sans-serif;
  }
  .sheet { position: relative; width: 804px; height: 1200px; }

  /* Front face */
  .card-front {
    position: absolute; left: 52px; top: 40px;
    width: 700px; height: 400px; overflow: hidden;
    box-shadow: 0 6px 18px rgba(0,0,0,.25);
  }
  .fabric-fill {
    position: absolute; inset: 0;
    background: radial-gradient(ellipse at 50% 50%, var(--denim-light) 0%, var(--denim-mid) 55%, var(--denim-deep) 100%);
  }
  .brand-lockup {
    position: absolute; left: 50%; top: 50%;
    transform: translate(-50%, -50%);
    display: flex; align-items: center; gap: 14px;
    white-space: nowrap;
  }
  .brand-dot {
    width: 22px; height: 22px; border-radius: 50%;
    background: var(--ink);
  }
  .brand-name {
    font-weight: 800; font-size: 34px; letter-spacing: -0.5px;
    color: var(--ink); text-transform: lowercase;
  }
  .front-bar { position: absolute; width: 6px; height: 62px; background: var(--ink); }
  .front-bar--upper { left: 150px; top: 70px; }
  .front-bar--lower { right: 150px; bottom: 70px; }

  /* Back face (portrait) */
  .card-back {
    position: absolute; left: 202px; top: 470px;
    width: 400px; height: 700px; overflow: hidden;
    background: linear-gradient(165deg, #000 0%, #000 38%, #1c1c1c 58%, var(--charcoal) 100%);
    box-shadow: 0 6px 18px rgba(0,0,0,.3);
    color: var(--paper-white);
  }
  .back-bar { position: absolute; height: 6px; width: 70px; background: var(--paper-white); }
  .back-bar--upper { left: 46px; top: 110px; }
  .back-bar--lower { right: 40px; bottom: 46px; }
  .holder-name {
    position: absolute; left: 46px; top: 230px;
    font-weight: 800; font-size: 84px; line-height: 0.86; letter-spacing: -3px;
    white-space: nowrap;
    text-shadow: 0 -14px 12px rgba(255,255,255,.18), 0 -30px 22px rgba(255,255,255,.1);
  }
  .holder-name span { display: block; }
  .contact-list {
    position: absolute; left: 46px; top: 470px;
    list-style: none; font-weight: 300; font-size: 19px; line-height: 1.55;
    letter-spacing: -0.3px; white-space: nowrap;
  }
  .contact-list b { font-weight: 800; }
  .back-brand {
    position: absolute; left: 46px; bottom: 36px;
    display: flex; align-items: center; gap: 8px;
    font-weight: 300; font-size: 12px; color: var(--muted);
  }
  .back-brand i { width: 12px; height: 12px; border-radius: 50%; background: var(--muted); display: block; }
</style>
</head>
<body>
<main class="sheet">
  <section class="card-front">
    <div class="fabric-fill" role="img" aria-label="Photograph of a blue plaid flannel shirt filling the card face"></div>
    <div class="front-bar front-bar--upper"></div>
    <div class="front-bar front-bar--lower"></div>
    <div class="brand-lockup">
      <span class="brand-dot"></span>
      <span class="brand-name">QM active wear</span>
    </div>
  </section>

  <section class="card-back">
    <div class="back-bar back-bar--upper"></div>
    <h1 class="holder-name"><span>Liam</span><span>Scott</span></h1>
    <ul class="contact-list">
      <li><b>T:</b> 002 345 6789</li>
      <li><b>M:</b> 002 345 6789</li>
      <li><b>E:</b> liam@qmactivewear.com</li>
      <li><b>S:</b> liam.scott</li>
      <li><b>W:</b> www.qmactivewear.com</li>
    </ul>
    <div class="back-brand"><i></i>QM Active Wear</div>
    <div class="back-bar back-bar--lower"></div>
  </section>
</main>
</body>
</html>
```